Design some Business Cards

Need some business cards made for new venture - website is vantrimo.com. I want to incorporate (in some fashion):

- logo (provided with name, and alone)
- website <p> font (Arvo )

Brian T. Holloway
BH VANTRIMO
817 E. Thornbury Ave. 3rd Floor
Chicago, IL 60648
brianh@vantrimo.com
(312) 555-0148
vantrimo.com

I am not very creative, hence the contest. Feel free to add design elements, but keep things consistent with the website (naturally). I am indifferent to one side vs. two-sided business card. I will be using CardNexa, so you will want to use their Illustrator (or photoshop) templates located here:

http://www.cardnexa-print.com/cn/ns/prodesk/UploadFiles.aspx?pf_id=Q41&selectedTab=0

The work product will be an Illustrator or Photoshop file, using the templates, with the winning design.

```html
<!DOCTYPE html>
<html lang="en">
<head>
<meta charset="utf-8">
<title>Vantrimo Business Cards</title>
<link href="https://fonts.googleapis.com/css2?family=Arvo:wght@700&family=PT+Sans:wght@400;700&display=swap" rel="stylesheet">
<style>
  :root {
    --stage: #3b3441;
    --card-white: #ffffff;
    --card-grey: #a4a4a4;
    --band-grey: #9c9c9c;
    --ink: #1c1c1c;
    --ink-soft: #333333;
  }
  * { box-sizing: border-box; margin: 0; padding: 0; }
  html, body { width: 1200px; height: 800px; overflow: hidden; }
  body {
    background: var(--stage);
    font-family: "PT Sans", Arial, sans-serif;
    color: var(--ink);
    position: relative;
  }
  .card {
    position: absolute;
    top: 240px;
    width: 520px;
    height: 300px;
    overflow: hidden;
    box-shadow: 0 10px 30px rgba(0,0,0,0.35);
  }

  /* Back side */
  .card--back { left: 50px; background: var(--card-grey); }
  .back-logo {
    position: absolute;
    left: 0; right: 0; top: 92px;
    display: flex; justify-content: center; align-items: center; gap: 14px;
  }
  .logo-dot {
    width: 30px; height: 30px; border-radius: 50%;
    background: var(--ink);
  }
  .wordmark {
    font-family: "Arvo", Georgia, serif;
    font-weight: 700;
    font-size: 34px;
    color: var(--ink);
    letter-spacing: 0.5px;
  }
  .back-address {
    position: absolute;
    left: 0; right: 0; top: 196px;
    display: flex; justify-content: center; align-items: center; gap: 8px;
    font-size: 16px;
    color: var(--ink);
  }

  /* Front side */
  .card--front { left: 630px; background: var(--card-white); }
  .front-id { position: absolute; left: 26px; top: 22px; }
  .person-name { font-size: 18px; font-weight: 400; color: var(--ink); }
  .person-title { font-size: 14px; color: var(--ink-soft); margin-top: 2px; letter-spacing: 0.5px; }
  .front-logo {
    position: absolute;
    left: 0; right: 0; top: 98px;
    display: flex; justify-content: center; align-items: center; gap: 14px;
  }
  .logo-divider { width: 2px; height: 38px; background: var(--ink); }
  .contact-band {
    position: absolute;
    left: 0; right: 0; bottom: 0; height: 108px;
    background: var(--band-grey);
    display: flex; justify-content: space-around; align-items: center;
    padding: 0 14px;
  }
  .contact-item {
    display: flex; flex-direction: column; align-items: center; gap: 10px;
    font-size: 14px; color: var(--ink);
  }
  .icon { width: 18px; height: 18px; }
</style>
</head>
<body>

  <section class="card card--back" aria-label="Business card back">
    <div class="back-logo">
      <span class="logo-dot"></span>
      <span class="wordmark">vantrimo</span>
    </div>
    <div class="back-address">
      <svg class="icon" viewBox="0 0 24 24" aria-hidden="true">
        <circle cx="12" cy="12" r="11" fill="#1c1c1c"/>
        <path d="M12 5a4 4 0 0 0-4 4c0 3 4 9 4 9s4-6 4-9a4 4 0 0 0-4-4z" fill="#a4a4a4"/>
        <circle cx="12" cy="9" r="1.5" fill="#1c1c1c"/>
      </svg>
      <span>817 E. Thornbury Ave. 3rd Floor, Chicago, IL 60648</span>
    </div>
  </section>

  <section class="card card--front" aria-label="Business card front">
    <div class="front-id">
      <p class="person-name">Brian T. Holloway</p>
      <p class="person-title">BH VANTRIMO</p>
    </div>
    <div class="front-logo">
      <span class="logo-dot"></span>
      <span class="logo-divider"></span>
      <span class="wordmark">vantrimo</span>
    </div>
    <div class="contact-band">
      <div class="contact-item">
        <svg class="icon" viewBox="0 0 24 24" aria-hidden="true">
          <path d="M6.6 10.8a15 15 0 0 0 6.6 6.6l2.2-2.2a1 1 0 0 1 1-.25 11.4 11.4 0 0 0 3.6.6 1 1 0 0 1 1 1V20a1 1 0 0 1-1 1A17 17 0 0 1 3 4a1 1 0 0 1 1-1h3.5a1 1 0 0 1 1 1c0 1.25.2 2.45.6 3.6a1 1 0 0 1-.25 1z" fill="#1c1c1c"/>
        </svg>
        <span>(312) 555-0148</span>
      </div>
      <div class="contact-item">
        <svg class="icon" viewBox="0 0 24 24" aria-hidden="true">
          <rect x="3" y="6" width="18" height="12" fill="none" stroke="#1c1c1c" stroke-width="1.6"/>
          <path d="M3 6l9 7 9-7" fill="none" stroke="#1c1c1c" stroke-width="1.6"/>
        </svg>
        <span>brianh@vantrimo.com</span>
      </div>
      <div class="contact-item">
        <svg class="icon" viewBox="0 0 24 24" aria-hidden="true">
          <path d="M3 12l9-8 9 8M6 10v10h12V10" fill="none" stroke="#1c1c1c" stroke-width="1.6"/>
        </svg>
        <span>vantrimo.com</span>
      </div>
    </div>
  </section>

</body>
</html>
```